Motorcycle Shop Business Card

New business card for Motorcycle repair and customization shop.Business name: Copper Falcon Chris Morris443-865-5190, 7214 Quarry Lane Harlow Ridge, MD 21990. www.dale@copperfalconcustoms.example. I uploaded some motorcycle images and logo and a couple of our calendar shoots. They do not have to be used on card just examples of some of our work and past graphic work.
We work on Vantor Brennick and Custom Built Motorcycles.

Looking for front and back design

Target Market(s)

Motorcycle owners

Industry/Entity Type

Motorcycle Part

```html
<!DOCTYPE html>
<html lang="en">
<head>
<meta charset="utf-8">
<title>Copper Falcon Customs – Business Cards</title>
<link rel="stylesheet" href="https://fonts.googleapis.com/css2?family=Montserrat:wght@500;600;800&display=swap">
<style>
  :root {
    --backdrop: #ebebeb;
    --card-black: #0b0b0b;
    --card-white: #fafafa;
    --ink-light: #ffffff;
    --ink-dark: #111111;
    --ghost: #262626;
    --rule: #8a8a8a;
  }
  * { margin: 0; padding: 0; box-sizing: border-box; }
  html, body { width: 1200px; height: 800px; overflow: hidden; }
  body {
    background: var(--backdrop);
    font-family: "Montserrat", Arial, sans-serif;
    position: relative;
  }
  .card {
    position: absolute;
    top: 278px;
    height: 240px;
    overflow: hidden;
  }

  /* Back side */
  .card-back {
    left: 142px;
    width: 418px;
    background: var(--card-black);
  }
  .card-back .ghost-name {
    position: absolute;
    left: 0; right: 0;
    top: 78px;
    text-align: center;
    font-weight: 800;
    font-size: 34px;
    letter-spacing: 1px;
    color: var(--ghost);
    text-transform: uppercase;
    line-height: 1.1;
  }
  .card-back .email-band {
    position: absolute;
    left: 0; right: 0;
    top: 195px;
    height: 29px;
    background: var(--card-white);
    color: var(--ink-dark);
    font-weight: 500;
    font-size: 13.5px;
    letter-spacing: 0.3px;
    display: flex;
    align-items: center;
    justify-content: center;
    white-space: nowrap;
  }

  /* Front side */
  .card-front {
    left: 638px;
    width: 420px;
    background: var(--card-white);
  }
  .card-front .brand-panel {
    position: absolute;
    left: 0; top: 0;
    width: 198px; height: 100%;
    display: flex;
    flex-direction: column;
    align-items: center;
    justify-content: center;
    text-align: center;
    color: var(--ink-dark);
    font-weight: 800;
    font-size: 19px;
    line-height: 1.15;
    text-transform: uppercase;
    letter-spacing: 0.5px;
  }
  .card-front .divider-bar {
    position: absolute;
    left: 200px; top: 0;
    width: 6px; height: 100%;
    background: var(--card-black);
  }
  .card-front .contact-panel {
    position: absolute;
    left: 209px; top: 0; right: 0; bottom: 0;
    background: var(--card-black);
    color: var(--ink-light);
    text-align: center;
  }
  .contact-panel .person-name {
    position: absolute;
    left: 0; right: 0; top: 42px;
    font-weight: 800;
    font-size: 20px;
    letter-spacing: 0.6px;
    white-space: nowrap;
  }
  .contact-panel .rule {
    position: absolute;
    left: 60px; right: 60px;
    height: 1px;
    background: var(--rule);
  }
  .contact-panel .rule-top { top: 88px; }
  .contact-panel .rule-bottom { top: 146px; }
  .contact-panel .phone {
    position: absolute;
    left: 0; right: 0; top: 106px;
    font-weight: 500;
    font-size: 12.5px;
    letter-spacing: 0.3px;
  }
  .contact-panel .address {
    position: absolute;
    left: 0; right: 0; top: 162px;
    font-weight: 500;
    font-size: 12.5px;
    line-height: 16px;
    letter-spacing: 0.2px;
    white-space: nowrap;
  }
</style>
</head>
<body>
  <section class="card card-back" aria-label="Card back">
    <div class="ghost-name">Copper Falcon<br>Customs</div>
    <div class="email-band">www.dale@copperfalconcustoms.example</div>
  </section>

  <section class="card card-front" aria-label="Card front">
    <div class="brand-panel">Copper Falcon<br>Customs</div>
    <div class="divider-bar"></div>
    <div class="contact-panel">
      <div class="person-name">DALE FENWICK</div>
      <div class="rule rule-top"></div>
      <div class="phone">410-555-0137</div>
      <div class="rule rule-bottom"></div>
      <div class="address">7214 Quarry Lane<br>Harlow Ridge, MD 21990.</div>
    </div>
  </section>
</body>
</html>
```